BN corporate design package (revamp our letterheads, business cards, envelopes, stationary designs)

About us
BrightNook is a multi-faceted company with a vision to create a niche in both Children’s Education & Family Entertainment industry. The Company aims at operating paramount schools, nurseries, indoor/outdoor play areas, and amusement centers, which will also be a hub for the entire family in the region and across the globe.

I would like to revamp our letterheads, business cards, envelopes, stationary designs. Fresh look with professionalism intact.

Target Market(s)

Clients, Parents, Job applicants

Industry/Entity Type

Entertainment

Font styles to use
Serif

Requirements
Must have
• Creative, out of the box designs

```html
<!DOCTYPE html>
<html lang="en">
<head>
<meta charset="utf-8">
<title>BrightNook Stationery</title>
<link rel="stylesheet" href="https://fonts.googleapis.com/css2?family=Tinos:wght@400;700&display=swap">
<style>
:root{
  --ink:#4a4646;
  --paper:#fbfbfb;
  --stage:#ffffff;
  --ghost:#e6e6e7;
  --dark:#4b4747;
  --sun:#f5a01a;
  --sky:#29a9e0;
  --berry:#d6338a;
}
*{box-sizing:border-box;margin:0;padding:0}
html,body{width:1200px;height:828px;overflow:hidden;background:var(--stage)}
body{font-family:"Tinos",serif;color:var(--ink);position:relative}
.sheet{position:absolute;background:var(--paper);overflow:hidden;border:1px solid #eee}
.brand{position:absolute;display:flex;align-items:center;gap:6px;font-family:"Tinos",serif;font-weight:700;color:var(--ink);white-space:nowrap;letter-spacing:-.5px}
.brand .dot{border-radius:50%;background:var(--sun);flex:none}
.ghost-word{position:absolute;font-family:"Tinos",serif;font-weight:700;color:var(--ghost);white-space:nowrap;letter-spacing:-2px;line-height:1}
.ghost-circle{position:absolute;border-radius:50%;background:var(--ghost)}
.contact{position:absolute;font-size:11px;line-height:14px;color:var(--ink)}
.contact .row{display:flex;align-items:center;gap:6px}
.contact svg{width:9px;height:9px;flex:none}
.badges{position:absolute;display:flex;align-items:center;gap:8px}
.badge-a{background:var(--sun);border-radius:6px}
.badge-b{background:var(--dark);border-radius:50%;border:3px solid var(--sun)}
.rule{position:absolute;width:2px;background:var(--ink)}
.dark{background:var(--dark);border-color:var(--dark)}
.dark .brand,.dark .contact{color:#fff}
</style>
</head>
<body>

<!-- Letterhead -->
<section class="sheet letterhead" style="left:88px;top:63px;width:486px;height:688px">
  <div class="brand" style="left:22px;top:70px;font-size:28px"><span class="dot" style="width:14px;height:14px"></span>BrightNook</div>
  <div class="rule" style="left:341px;top:30px;height:93px"></div>
  <div class="contact" style="left:354px;top:32px;font-size:10.5px">
    <div>PO Box 204817</div><div>Harbour City</div>
    <div class="row" style="margin-top:3px"><svg viewBox="0 0 10 10"><rect x="2" y="0" width="6" height="10" rx="1" fill="currentColor"/><rect x="3" y="1.5" width="4" height="6" fill="#fff"/></svg>+00 2 555 0148</div>
    <div class="row"><svg viewBox="0 0 10 10"><rect x="0" y="2" width="10" height="7" fill="currentColor"/><path d="M0 2l5 4 5-4" stroke="#fff" fill="none"/></svg>info@brightnook.net</div>
    <div>www.brightnook.net</div>
  </div>
  <div class="ghost-circle" role="img" aria-label="Faint brand decoration" style="left:290px;top:430px;width:120px;height:120px"></div>
  <div class="ghost-word" style="left:20px;top:590px;font-size:110px">BrightN</div>
  <div class="badges" style="left:178px;top:618px">
    <div class="badge-a" role="img" aria-label="Partner badge" style="width:62px;height:34px"></div>
    <div class="badge-b" role="img" aria-label="Partner badge" style="width:54px;height:54px"></div>
  </div>
</section>

<!-- Business card front -->
<section class="sheet card" style="left:122px;top:270px;width:205px;height:116px">
  <div class="ghost-circle" role="img" aria-label="Faint brand decoration" style="left:120px;top:8px;width:42px;height:42px"></div>
  <div class="ghost-word" style="left:50px;top:78px;font-size:44px">Bright</div>
  <div class="brand" style="left:14px;top:22px;font-size:14px"><span class="dot" style="width:7px;height:7px"></span>BrightNook</div>
  <div class="contact" style="left:16px;top:72px;font-size:9px;line-height:10px"><div>Mara Delacroix</div><div style="font-size:6px">Director</div></div>
  <div class="contact" style="left:118px;top:52px;font-size:6px;line-height:8px">
    <div>PO Box 204817</div><div>Harbour City</div><div>+00 2 555 0148</div><div>info@brightnook.net</div><div>www.brightnook.net</div>
  </div>
</section>

<!-- Business card back -->
<section class="sheet card dark" style="left:326px;top:255px;width:222px;height:124px">
  <div class="brand" style="left:52px;top:44px;font-size:22px"><span class="dot" style="width:10px;height:10px"></span>BrightNook</div>
  <div class="badges" style="left:92px;top:90px;gap:5px">
    <div class="badge-a" role="img" aria-label="Partner badge" style="width:24px;height:14px"></div>
    <div class="badge-b" role="img" aria-label="Partner badge" style="width:20px;height:20px;border-width:2px"></div>
  </div>
</section>

<!-- Envelope back -->
<section class="sheet envelope" style="left:612px;top:64px;width:510px;height:255px">
  <div class="brand" style="left:22px;top:62px;font-size:28px"><span class="dot" style="width:14px;height:14px"></span>BrightNook</div>
  <div class="ghost-circle" role="img" aria-label="Faint brand decoration" style="left:310px;top:50px;width:110px;height:110px"></div>
  <div class="contact" style="left:24px;top:170px;font-size:10.5px">
    <div>PO Box 204817</div><div>Harbour City</div>
    <div class="row" style="margin-top:3px"><svg viewBox="0 0 10 10"><rect x="2" y="0" width="6" height="10" rx="1" fill="currentColor"/><rect x="3" y="1.5" width="4" height="6" fill="#fff"/></svg>+00 2 555 0148</div>
    <div class="row"><svg viewBox="0 0 10 10"><rect x="0" y="2" width="10" height="7" fill="currentColor"/><path d="M0 2l5 4 5-4" stroke="#fff" fill="none"/></svg>info@brightnook.net</div>
    <div>www.brightnook.net</div>
  </div>
</section>

<!-- Envelope front -->
<section class="sheet envelope" style="left:598px;top:330px;width:535px;height:245px;box-shadow:0 -4px 10px rgba(0,0,0,.08)">
  <div class="brand" style="left:28px;top:60px;font-size:28px"><span class="dot" style="width:14px;height:14px"></span>BrightNook</div>
  <div class="ghost-circle" role="img" aria-label="Faint brand decoration" style="left:340px;top:30px;width:110px;height:110px"></div>
  <div class="ghost-word" style="left:130px;top:190px;font-size:90px">BrightNo</div>
  <div class="contact" style="left:30px;top:160px;font-size:10.5px">
    <div>PO Box 204817</div><div>Harbour City</div>
    <div class="row" style="margin-top:3px"><svg viewBox="0 0 10 10"><rect x="2" y="0" width="6" height="10" rx="1" fill="currentColor"/><rect x="3" y="1.5" width="4" height="6" fill="#fff"/></svg>+00 2 555 0148</div>
    <div class="row"><svg viewBox="0 0 10 10"><rect x="0" y="2" width="10" height="7" fill="currentColor"/><path d="M0 2l5 4 5-4" stroke="#fff" fill="none"/></svg>info@brightnook.net</div>
    <div>www.brightnook.net</div>
  </div>
  <div class="badges" style="left:410px;top:150px">
    <div class="badge-a" role="img" aria-label="Partner badge" style="width:54px;height:30px"></div>
    <div class="badge-b" role="img" aria-label="Partner badge" style="width:46px;height:46px"></div>
  </div>
</section>

<!-- Email signature light -->
<section class="sheet signature" style="left:697px;top:598px;width:288px;height:62px">
  <div class="brand" style="left:10px;top:22px;font-size:14px"><span class="dot" style="width:7px;height:7px"></span>BrightNook</div>
  <div class="rule" style="left:98px;top:6px;height:50px;width:1px"></div>
  <div class="contact" style="left:106px;top:7px;font-size:6.5px;line-height:8px">
    <div style="font-size:7.5px">Mara Delacroix</div><div style="font-size:5px">Director</div>
    <div>PO Box 204817, Harbour City</div><div>+00 2 555 0148</div><div>info@brightnook.net</div><div>www.brightnook.net</div>
  </div>
  <div class="badges" style="left:203px;top:16px;gap:5px">
    <div class="badge-a" role="img" aria-label="Partner badge" style="width:36px;height:22px"></div>
    <div class="badge-b" role="img" aria-label="Partner badge" style="width:34px;height:34px;border-width:2px"></div>
  </div>
</section>

<!-- Email signature dark -->
<section class="sheet signature dark" style="left:697px;top:676px;width:288px;height:61px">
  <div class="brand" style="left:10px;top:22px;font-size:14px"><span class="dot" style="width:7px;height:7px"></span>BrightNook</div>
  <div class="rule" style="left:98px;top:6px;height:50px;width:1px;background:#fff"></div>
  <div class="contact" style="left:106px;top:7px;font-size:6.5px;line-height:8px">
    <div style="font-size:7.5px">Mara Delacroix</div><div style="font-size:5px">Director</div>
    <div>PO Box 204817, Harbour City</div><div>+00 2 555 0148</div><div>info@brightnook.net</div><div>www.brightnook.net</div>
  </div>
  <div class="badges" style="left:203px;top:15px;gap:5px">
    <div class="badge-a" role="img" aria-label="Partner badge" style="width:36px;height:22px"></div>
    <div class="badge-b" role="img" aria-label="Partner badge" style="width:34px;height:34px;border-width:2px"></div>
  </div>
</section>

</body>
</html>
```